Global Nano Technology Surface Protection company needs a new logo and cards

We are a Global company that will apply nanotechnology coatings on surfaces to prevent growth and spread of bacteria, viruses, mold etc. We deal with large corporates, airlines, hospitals and schools so we are after a new modern, simple and clean look that will have great visual impact.
We a company that is focused on prevention and protection.

Company name, Luminary Fabrications Worldwide

Subtext, Antimicrobial Surface Protection

Logo, LFWW or LFW

Target Market(s)

Hospitals, Transport agencies, Airlines, Corporate entities

Industry/Entity Type

Protection

Contact Information for Business Card

Logo, LFWW or LFW
www.lfww.us
Derek Hawtrey
+64213958260
tidyshieldnz@mailbox.example

Logo Text

LFWW

Requirements
Must have
• Simple clean look
Should not have
• Nothing too messy

```html
<!DOCTYPE html>
<html lang="en">
<head>
<meta charset="utf-8">
<title>Luminary Fabrications Worldwide — Business Cards</title>
<link href="https://fonts.googleapis.com/css2?family=Montserrat:wght@500;600;700&family=Arimo:wght@400&display=swap" rel="stylesheet">
<style>
  :root {
    --bg: #e4e5e8;
    --card-dark: #2a2a2a;
    --card-dark-edge: #333333;
    --card-light-edge: #d6d6d6;
    --ribbon: #a3dd7c;
    --ribbon-fold: #6fa84a;
    --ink-dark: #1f1f1f;
    --ink-light: #d9d9d9;
    --accent: #5fcf9c;
  }
  * { margin: 0; padding: 0; box-sizing: border-box; }
  html, body { width: 1200px; height: 800px; overflow: hidden; }
  body { background: var(--bg); position: relative; font-family: "Montserrat", sans-serif; }

  .card {
    position: absolute;
    left: 320px;
    width: 560px;
    height: 320px;
    overflow: hidden;
  }

  /* Front */
  .card-front {
    top: 60px;
    background: linear-gradient(135deg, var(--card-dark) 0%, var(--card-dark-edge) 100%);
  }
  .front-wordmark {
    position: absolute;
    left: 98px;
    top: 106px;
    color: var(--ink-light);
  }
  .front-name {
    font-weight: 500;
    font-size: 28px;
    line-height: 35px;
    letter-spacing: 0.2px;
    text-transform: uppercase;
  }
  .front-tagline {
    font-weight: 500;
    font-size: 11.5px;
    letter-spacing: 0.6px;
    word-spacing: 4px;
    margin-top: 4px;
    text-transform: uppercase;
    white-space: nowrap;
  }
  .front-mark {
    position: absolute;
    left: 404px;
    top: 142px;
    width: 34px;
    height: 34px;
    border-radius: 50%;
    background: var(--accent);
  }

  /* Back */
  .card-back {
    top: 420px;
    background: linear-gradient(135deg, #eeeeee 0%, var(--card-light-edge) 100%);
  }
  .back-panel {
    position: absolute;
    left: 319px;
    top: 0;
    right: 0;
    bottom: 0;
    background: var(--card-dark);
  }
  .back-logo {
    position: absolute;
    left: 63px;
    top: 130px;
    display: flex;
    align-items: center;
    gap: 14px;
  }
  .back-logo-text {
    font-weight: 600;
    font-size: 56px;
    line-height: 64px;
    color: var(--ink-dark);
    letter-spacing: 1px;
  }
  .back-logo-mark {
    width: 34px;
    height: 34px;
    border-radius: 50%;
    background: var(--accent);
  }

  .ribbon {
    position: absolute;
    left: 297px;
    right: 0;
    background: var(--ribbon);
    display: flex;
    align-items: center;
    white-space: nowrap;
  }
  .ribbon::after {
    content: "";
    position: absolute;
    left: 0;
    top: 100%;
    width: 22px;
    height: 20px;
    background: var(--ribbon-fold);
    clip-path: polygon(0 0, 100% 0, 100% 100%);
  }
  .ribbon-name {
    top: 26px;
    height: 44px;
    justify-content: center;
    padding-left: 22px;
    font-weight: 700;
    font-size: 21px;
    color: var(--ink-dark);
    letter-spacing: 0.3px;
    text-transform: uppercase;
  }
  .ribbon-contact {
    height: 32px;
    padding-left: 26px;
    font-family: "Arimo", sans-serif;
    font-size: 13px;
    color: var(--ink-dark);
  }
  .ribbon-phone { top: 109px; }
  .ribbon-web { top: 178px; }
  .ribbon-mail { top: 241px; height: 34px; }
  .contact-icon {
    width: 17px;
    height: 17px;
    margin-right: 10px;
    flex: none;
  }
</style>
</head>
<body>
  <section class="card card-front" aria-label="Business card front">
    <div class="front-wordmark">
      <div class="front-name">Luminary<br>Fabrications<br>Worldwide</div>
      <div class="front-tagline">Antimicrobial Surface Protection</div>
    </div>
    <div class="front-mark"></div>
  </section>

  <section class="card card-back" aria-label="Business card back">
    <div class="back-logo">
      <span class="back-logo-text">LFW</span>
      <span class="back-logo-mark"></span>
    </div>
    <div class="back-panel"></div>

    <div class="ribbon ribbon-name">Derek Hawtrey</div>

    <div class="ribbon ribbon-contact ribbon-phone">
      <svg class="contact-icon" viewBox="0 0 24 24" aria-hidden="true">
        <path d="M6.6 2.5l3 3.2-1.8 2.6c.9 2.6 3.1 4.8 5.7 5.7l2.6-1.8 3.2 3-1.8 3.3C11 18.8 5.2 13 4.3 4.3z" fill="#1f1f1f"/>
      </svg>
      +64213958260
    </div>

    <div class="ribbon ribbon-contact ribbon-web">
      <svg class="contact-icon" viewBox="0 0 24 24" aria-hidden="true">
        <circle cx="12" cy="12" r="9.5" fill="none" stroke="#1f1f1f" stroke-width="2"/>
        <ellipse cx="12" cy="12" rx="4" ry="9.5" fill="none" stroke="#1f1f1f" stroke-width="1.6"/>
        <line x1="2.5" y1="12" x2="21.5" y2="12" stroke="#1f1f1f" stroke-width="1.6"/>
      </svg>
      www.lfww.us
    </div>

    <div class="ribbon ribbon-contact ribbon-mail">
      <svg class="contact-icon" viewBox="0 0 24 24" aria-hidden="true">
        <rect x="2" y="5" width="20" height="14" fill="#1f1f1f"/>
        <path d="M2.5 5.5L12 13l9.5-7.5" fill="none" stroke="#a3dd7c" stroke-width="1.6"/>
      </svg>
      tidyshieldnz@mailbox.example
    </div>
  </section>
</body>
</html>
```